Brightfold Partners Website

Brightfold Partners (BP) provide Analytics & Enterprise Performance Management (EPM) advisory & consultancy services. We are passionate about data and making a difference for our clients by working in partnership with them, helping them on their journey to becoming an Brightfold Partner. We deliver insights which give our clients a competitive edge and a much deeper understanding of their organisation.

We need a website which shows who we are, what we do and how we do it.

www.brightfold-partners.example is our very basic website at the moment. We want to completely revamp it with a corporate look

```html
<!DOCTYPE html>
<html lang="en">
<head>
<meta charset="utf-8">
<title>Brightfold Partners</title>
<link href="https://fonts.googleapis.com/css2?family=Poppins:wght@400;500;600;700&display=swap" rel="stylesheet">
<style>
:root{
  --navy:#1b2b38;
  --steel:#2b5570;
  --orange:#d8672f;
  --mist:#eef5f8;
  --text:#5b6670;
  --white:#ffffff;
}
*{margin:0;padding:0;box-sizing:border-box}
html,body{width:1200px;height:2595px;overflow:hidden}
body{font-family:'Poppins',sans-serif;background:var(--white);position:relative;color:var(--text)}
.abs{position:absolute}
.btn{position:absolute;display:flex;align-items:center;justify-content:center;gap:6px;border-radius:20px;font-size:13px;text-transform:uppercase;background:var(--orange);color:var(--white);height:37px}
.label{position:absolute;font-size:12px;color:var(--orange);text-transform:uppercase}
.heading{position:absolute;font-weight:600;color:var(--navy);text-transform:uppercase;font-size:27px;line-height:37px}
.para{position:absolute;font-size:14.5px;line-height:22.5px;color:var(--text)}
.brand{position:absolute;display:flex;align-items:center;gap:14px;color:var(--white);font-weight:600;font-size:20px;line-height:22px;text-transform:uppercase}
.brand-dot{width:52px;height:52px;border-radius:50%;border:5px solid var(--white)}

/* hero */
.hero{position:absolute;left:0;top:0;width:1200px;height:600px;background:var(--navy)}
.hero-photo{position:absolute;left:600px;top:0;width:600px;height:600px;background:linear-gradient(160deg,#cfdce6 0%,#6f9cc0 40%,#2d5f8c 75%,#1e4466 100%)}
.nav{position:absolute;top:28px;left:654px;display:flex;gap:36px;font-size:12.5px;color:var(--white);text-transform:uppercase}
.hero-title{position:absolute;left:61px;top:185px;font-size:51px;line-height:61px;font-weight:700;color:var(--white);text-transform:uppercase}
.hero-sub{position:absolute;left:61px;top:316px;font-size:14px;color:var(--white)}
.hero-arrow{position:absolute;left:567px;top:254px;width:66px;height:66px;border-radius:50%;border:1px solid rgba(255,255,255,.8);display:flex;align-items:center;justify-content:center}
.hero-arrow span{width:54px;height:54px;border-radius:50%;background:var(--white);display:flex;align-items:center;justify-content:center}

/* about */
.team-photo{position:absolute;left:60px;top:662px;width:375px;height:375px;border-radius:50%;background:radial-gradient(circle at 45% 40%,#c9a98f 0%,#8b7a70 35%,#3b5b72 70%,#2b5570 100%)}

/* services */
.services{position:absolute;left:0;top:1120px;width:1200px;height:477px;background:var(--mist)}
.card{position:absolute;top:125px;width:340px;height:300px;background:var(--white);border-radius:14px;text-align:center;padding-top:31px}
.card.featured{background:var(--navy)}
.card-icon{width:68px;height:68px;border-radius:50%;background:var(--navy);margin:0 auto;display:flex;align-items:center;justify-content:center}
.featured .card-icon{background:var(--white)}
.card h3{font-weight:500;font-size:17px;color:var(--navy);margin-top:28px}
.featured h3{color:var(--white)}
.card p{font-size:14px;line-height:22.5px;color:var(--text);margin:6px auto 0;width:290px;height:92px}
.featured p{color:var(--white)}
.card .more{font-size:13px;color:var(--orange);text-transform:uppercase;margin-top:10px;display:inline-flex;gap:4px;align-items:center}

/* cta */
.footer-band{position:absolute;left:0;top:2220px;width:1200px;height:338px;background:var(--navy)}
.cta{position:absolute;left:60px;top:2128px;width:1080px;height:175px;background:var(--steel);border-radius:20px}
.cta h2{position:absolute;left:42px;top:42px;font-size:27px;font-weight:600;color:var(--white)}
.cta p{position:absolute;left:42px;top:88px;width:600px;font-size:14px;line-height:22.5px;color:var(--white)}
.btn.light{background:var(--white);color:var(--navy);text-transform:none}

/* footer */
.foot-col h4{position:absolute;font-size:14px;font-weight:500;color:var(--white)}
.foot-col h4::after{content:"";display:block;width:72px;height:1px;background:rgba(255,255,255,.5);margin-top:8px}
.foot-link{position:absolute;font-size:11.5px;color:var(--white);text-transform:uppercase}
.foot-text{position:absolute;font-size:12px;line-height:20px;color:var(--white)}
.social{position:absolute;top:2472px;width:34px;height:34px;border-radius:50%}
.bottom-bar{position:absolute;left:0;top:2558px;width:1200px;height:37px;background:var(--orange);color:var(--white);font-size:12px;display:flex;align-items:center;justify-content:center}
</style>
</head>
<body>

<header class="hero">
  <div class="hero-photo" role="img" aria-label="Upward view of glass office towers against a cloudy sky"></div>
  <div class="brand" style="left:60px;top:14px"><span class="brand-dot"></span><span>Brightfold<br>Partners</span></div>
  <nav class="nav"><span>Who we are</span><span>What we do</span><span>How we do it</span></nav>
  <div class="btn" style="left:1007px;top:19px;width:133px;font-weight:600;font-size:13px">
    <svg width="18" height="18" viewBox="0 0 24 24" fill="none" stroke="#fff" stroke-width="1.8"><path d="M5 3h4l2 5-2.5 1.5a11 11 0 0 0 6 6L16 13l5 2v4a2 2 0 0 1-2 2A17 17 0 0 1 3 5a2 2 0 0 1 2-2z"/></svg>01 555 0142
  </div>
  <h1 class="hero-title">Brightfold<br>Partners</h1>
  <p class="hero-sub">DATA ANALYTICS &amp; EPM Consulting Services</p>
  <div class="btn" style="left:61px;top:397px;width:117px">Contact us</div>
  <div class="hero-arrow"><span><svg width="28" height="14" viewBox="0 0 28 14" fill="none" stroke="#1b2b38" stroke-width="2"><path d="M1 7h25M20 1l6 6-6 6"/></svg></span></div>
</header>

<section class="about">
  <div class="team-photo" role="img" aria-label="Team of three colleagues working together at a laptop"></div>
  <p class="label" style="left:609px;top:720px">Who we are</p>
  <h2 class="heading" style="left:609px;top:740px">Welcome to Brightfold<br>Partners</h2>
  <p class="para" style="left:611px;top:815px;width:425px">BP are a Data Analytics &amp; EPM company, specialising in the implementation and support of Business Intelligence, EPM and Data Analytics business solutions, both in the Cloud and on-premise.</p>
  <div class="btn" style="left:605px;top:940px;width:107px">Read more</div>
</section>

<section class="services">
  <p class="label" style="left:0;width:1200px;text-align:center;top:53px">Our services</p>
  <h2 class="heading" style="left:0;width:1200px;text-align:center;top:76px">What we do</h2>
  <article class="card" style="left:60px">
    <div class="card-icon"><svg width="34" height="34" viewBox="0 0 34 34" fill="none" stroke="#fff" stroke-width="1.5"><rect x="3" y="5" width="28" height="19" rx="2"/><path d="M13 29h8M17 24v5"/><circle cx="17" cy="12" r="4"/><path d="M10 22c1-4 4-5 7-5s6 1 7 5"/></svg></div>
    <h3>Advise &amp; Architech</h3>
    <p>Helping our customers understand the art of the possible and safeguarding their investments by overseeing implementations.</p>
    <span class="more">Read more <svg width="8" height="12" viewBox="0 0 8 12" fill="none" stroke="#d8672f" stroke-width="1.5"><path d="M1 1l5 5-5 5"/></svg></span>
  </article>
  <article class="card featured" style="left:430px">
    <div class="card-icon"><svg width="34" height="34" viewBox="0 0 34 34" fill="none" stroke="#1b2b38" stroke-width="1.5"><rect x="3" y="5" width="28" height="19" rx="2"/><path d="M13 29h8M17 24v5M9 20v-8M14 20v-10M19 20v-6M24 20v-9"/></svg></div>
    <h3>Design &amp; Implement</h3>
    <p>Working with the project management team, through each stage of the project, with clearly defined deliverables and well exercised plans to deliver them.</p>
    <span class="more">Read more <svg width="8" height="12" viewBox="0 0 8 12" fill="none" stroke="#d8672f" stroke-width="1.5"><path d="M1 1l5 5-5 5"/></svg></span>
  </article>
  <article class="card" style="left:800px">
    <div class="card-icon"><svg width="34" height="34" viewBox="0 0 34 34" fill="none" stroke="#fff" stroke-width="1.5"><rect x="3" y="5" width="24" height="20" rx="2"/><circle cx="20" cy="19" r="6"/><path d="M24 23l6 6M17 21v-3M20 21v-5M23 21v-2"/></svg></div>
    <h3>Optimse&amp;Manage</h3>
    <p>Our Managed Services delivers proactive, on-demand support for EPM and Data Analytics environments:</p>
    <span class="more">Read more <svg width="8" height="12" viewBox="0 0 8 12" fill="none" stroke="#d8672f" stroke-width="1.5"><path d="M1 1l5 5-5 5"/></svg></span>
  </article>
</section>

<section class="process">
  <p class="label" style="left:61px;top:1726px">Process</p>
  <h2 class="heading" style="left:61px;top:1750px">How we do it</h2>
  <p class="para" style="left:61px;top:1786px;width:500px">Lorem Ipsum is simply dummy text of the printing and typesetting industry. Lorem Ipsum has been the industry's standard dummy text ever since the 1500s, when an unknown printer took a galley of type and scrambled it to make a type specimen book. It has survived not only five centuries, but also the leap into electronic typesetting, remaining essentially unchanged.</p>
  <div class="btn" style="left:60px;top:1960px;width:107px">Read more</div>

  <svg class="abs" style="left:0;top:0" width="1200" height="2595" viewBox="0 0 1200 2595" aria-label="Three-step cycle: Idea, Plan, Growth">
    <g stroke="#fff" stroke-width="8" stroke-linejoin="round">
      <path fill="#d8672f" d="M749.2 1956 A188 188 0 0 1 918.6 1674.1 L914.9 1779 A83 83 0 0 0 840.1 1903.5 Z"/>
      <path fill="#2b5570" d="M918.6 1674.1 A188 188 0 0 1 1074.8 1956 L983.9 1903.5 A83 83 0 0 0 914.9 1779 Z"/>
      <path fill="#1b2b38" d="M1074.8 1956 A188 188 0 0 1 749.2 1956 L840.1 1903.5 A83 83 0 0 0 983.9 1903.5 Z"/>
    </g>
    <circle cx="912" cy="1862" r="80" fill="#eef3f6"/>
    <g font-family="Poppins, sans-serif" fill="#fff">
      <text x="835" y="1740" font-size="30" font-weight="600" transform="rotate(40 850 1730)">01</text>
      <circle cx="814" cy="1776" r="28" fill="rgba(255,255,255,.18)"/>
      <circle cx="814" cy="1773" r="11" fill="none" stroke="#fff" stroke-width="1.8"/>
      <path d="M809 1786h10" stroke="#fff" stroke-width="1.8"/>
      <text x="768" y="1810" font-size="17" transform="rotate(35 780 1810)">Idea</text>
      <text x="988" y="1768" font-size="30" font-weight="600">03</text>
      <circle cx="1024" cy="1800" r="28" fill="rgba(255,255,255,.18)"/>
      <path d="M1010 1814v-8M1018 1814v-13M1026 1814v-10M1034 1814v-16M1008 1802l18-14" stroke="#fff" stroke-width="1.8" fill="none"/>
      <text x="1020" y="1856" font-size="17" transform="rotate(-25 1045 1850)">Growth</text>
      <text x="826" y="1983" font-size="30" font-weight="600">02</text>
      <circle cx="903" cy="1990" r="26" fill="rgba(255,255,255,.1)"/>
      <rect x="890" y="1974" width="26" height="32" rx="3" fill="none" stroke="#fff" stroke-width="1.6"/>
      <path d="M895 1983h2M902 1983h9M895 1991h2M902 1991h9M895 1999h2M902 1999h9" stroke="#fff" stroke-width="1.6"/>
      <text x="946" y="1997" font-size="17" font-weight="500">Plan</text>
    </g>
  </svg>
</section>

<div class="footer-band"></div>

<section class="cta">
  <h2>Contact Us to Discuss Your Business Needs</h2>
  <p>Lorem Ipsum is simply dummy text of the printing and typesetting industry. Lorem Ipsum has been the industry's</p>
  <div class="btn" style="left:735px;top:69px;width:133px;font-weight:600;text-transform:none">
    <svg width="18" height="18" viewBox="0 0 24 24" fill="none" stroke="#fff" stroke-width="1.8"><path d="M5 3h4l2 5-2.5 1.5a11 11 0 0 0 6 6L16 13l5 2v4a2 2 0 0 1-2 2A17 17 0 0 1 3 5a2 2 0 0 1 2-2z"/></svg>01 555 0142
  </div>
  <div class="btn light" style="left:889px;top:69px;width:108px">Contact Us</div>
</section>

<footer>
  <div class="brand" style="left:60px;top:2350px"><span class="brand-dot"></span><span>Brightfold<br>Partners</span></div>
  <p class="foot-text" style="left:61px;top:2415px;width:250px">BP are a Data Analytics &amp; EPM company, specialising in the implementation.</p>
  <span class="social" style="left:60px;border:1.5px solid #fff" role="img" aria-label="Social profile link"></span>
  <span class="social" style="left:107px;background:var(--orange)" role="img" aria-label="Professional network link"></span>

  <div class="foot-col">
    <h4 style="left:338px;top:2361px">Quick Links</h4>
    <span class="foot-link" style="left:338px;top:2406px">Who we are</span>
    <span class="foot-link" style="left:338px;top:2437px">What we do</span>
    <span class="foot-link" style="left:338px;top:2469px">How we do it</span>
    <span class="foot-link" style="left:338px;top:2500px">Contact us</span>
  </div>

  <div class="foot-col">
    <h4 style="left:616px;top:2361px">Contact Us</h4>
    <svg class="abs" style="left:614px;top:2410px" width="18" height="22" viewBox="0 0 18 22" fill="none" stroke="#fff" stroke-width="1.4"><path d="M9 21s7-7 7-12A7 7 0 0 0 2 9c0 5 7 12 7 12z"/><circle cx="9" cy="9" r="2.5"/></svg>
    <p class="foot-text" style="left:644px;top:2405px;width:230px">12 Harbour Row, Quayside,<br>Dublin 4, D04 KX19</p>
    <svg class="abs" style="left:614px;top:2457px" width="18" height="18" viewBox="0 0 24 24" fill="none" stroke="#fff" stroke-width="1.6"><path d="M5 3h4l2 5-2.5 1.5a11 11 0 0 0 6 6L16 13l5 2v4a2 2 0 0 1-2 2A17 17 0 0 1 3 5a2 2 0 0 1 2-2z"/></svg>
    <p class="foot-text" style="left:644px;top:2457px;font-weight:600">01 555 0142</p>
    <svg class="abs" style="left:614px;top:2496px" width="20" height="15" viewBox="0 0 20 15" fill="none" stroke="#fff" stroke-width="1.4"><rect x="1" y="1" width="18" height="13"/><path d="M1 1l9 7 9-7"/></svg>
    <p class="foot-text" style="left:644px;top:2492px">info@brightfold-partners.example</p>
  </div>

  <div class="foot-col">
    <h4 style="left:891px;top:2361px">Our Partner</h4>
    <span class="abs" style="left:891px;top:2405px;width:130px;height:30px;border-radius:4px;background:rgba(255,255,255,.12)" role="img" aria-label="Technology partner badge"></span>
  </div>

  <div class="bottom-bar">2022©&nbsp;<strong style="font-weight:600">BRIGHTFOLD PARTNERS</strong>. All right reserved.</div>
</footer>

</body>
</html>
```